New business card design
Brovalco Upkeep LLC
Project: New business card design
New business card design -
Creative Brief
Professional
Darrel Wickham
President & CEO
2847 Tallow Bend Rd Norristown PA 19403
wwwdw@brovalco-example.com
www.brovalco-example.com
* Professionally done for less than the rest * Commercial & Residential;Interior & Exterior Window washing/Cleaning, Green House,Skylight,Gutter,Power washing services,Customized cleaning programs,Fully licensed, insured, and bonded professionals.

```html
<!DOCTYPE html>
<html lang="en">
<head>
<meta charset="utf-8">
<title>Brovalco Upkeep LLC — Stationery Set</title>
<link href="https://fonts.googleapis.com/css2?family=Arimo:wght@400;700&display=swap" rel="stylesheet">
<style>
  :root{
    --board:#2b2b2b;
    --blue:#1f5fae;
    --blue-deep:#123f7a;
    --blue-light:#3e86d6;
    --orange:#f08a1c;
    --paper:#ffffff;
    --paper-shade:#eef1f5;
    --ink:#1d2a3a;
    --muted:#6b7685;
    --label:#9a9a9a;
  }
  *{box-sizing:border-box;margin:0;padding:0}
  html,body{width:1200px;height:437px;overflow:hidden;background:var(--board);font-family:"Arimo",Arial,sans-serif}
  .board{position:relative;width:1200px;height:437px}
  .piece{position:absolute;background:var(--paper);box-shadow:0 2px 6px rgba(0,0,0,.5);overflow:hidden}
  .label{position:absolute;color:var(--label);font-size:7px;text-align:center}
  .band{position:absolute;left:0;width:100%;display:block}
  .brand{position:absolute;display:flex;align-items:center;gap:4px;color:var(--blue-deep);font-weight:700;white-space:nowrap;line-height:1}
  .brand .mark{width:8px;height:8px;background:var(--orange);flex:none}

  /* business cards */
  .card{left:19px;width:173px;height:98px}
  .card-front{top:30px}
  .card-front .brand{left:8px;top:60px;font-size:9px}
  .card-front .brand .mark{width:6px;height:6px}
  .card-front .person{position:absolute;left:84px;top:8px;width:84px;font-size:4.4px;color:var(--ink);line-height:1.4;white-space:nowrap}
  .card-front .person strong{display:block;font-size:6.2px;color:var(--blue-deep);margin-bottom:1px}
  .card-back{top:148px;background:linear-gradient(160deg,var(--blue-light),var(--blue-deep));color:#fff;padding:10px}
  .card-back-alt{top:266px;color:var(--ink);padding:10px}
  .card h3{font-size:6.5px;font-weight:700;margin-bottom:5px}
  .card-back-alt h3{color:var(--blue-deep)}
  .card ul{list-style:none;font-size:4.6px;line-height:1.5}
  .card ul li::before{content:"• ";color:var(--orange)}
  .card-back-alt ul{columns:2}

  /* letterheads */
  .letterhead{top:29px;width:272px;height:374px}
  .lh-1{left:204px}
  .lh-2{left:509px}
  .letterhead .brand{left:18px;top:58px;font-size:12px}
  .lh-contact{position:absolute;left:130px;top:14px;font-size:4.6px;line-height:1.6;color:#fff;white-space:nowrap}
  .lh-footer{position:absolute;bottom:9px;width:100%;text-align:center;font-size:4.4px;color:var(--muted)}

  /* envelopes */
  .envelope{left:888px;width:293px;height:92px}
  .env-back{top:29px}
  .env-plain-1{top:145px}
  .env-plain-2{top:244px}
  .env-front{top:323px}
  .env-front .brand{left:14px;top:40px;font-size:12px}
  .env-url{position:absolute;left:0;right:0;text-align:center;font-size:4.4px;color:var(--muted)}
</style>
</head>
<body>
<main class="board">

  <section class="piece card card-front">
    <svg class="band" style="bottom:0" width="173" height="22" viewBox="0 0 173 22" preserveAspectRatio="none">
      <path d="M0 10 Q90 2 173 6 V22 H0Z" fill="var(--blue)"/>
      <path d="M0 10 Q90 2 173 6" stroke="var(--orange)" stroke-width="1.5" fill="none"/>
    </svg>
    <div class="person"><strong>Darrel Wickham</strong>President &amp; CEO<br>2847 Tallow Bend Rd<br>Norristown PA 19403<br>wwwdw@brovalco-example.com<br>www.brovalco-example.com<br>darrel7171</div>
    <div class="brand"><span class="mark"></span>Brovalco Upkeep LLC</div>
  </section>
  <p class="label" style="left:19px;top:132px;width:173px">Front Card</p>

  <section class="piece card card-back">
    <h3>Professionally done for less than the rest</h3>
    <ul>
      <li>Commercial &amp; Residential</li>
      <li>Interior &amp; Exterior Window washing</li>
      <li>Green House, Skylight, Gutter</li>
      <li>Power washing services</li>
      <li>Customized cleaning programs</li>
      <li>Fully licensed, insured and bonded</li>
    </ul>
  </section>
  <p class="label" style="left:19px;top:250px;width:173px">Back Card Option #1</p>

  <section class="piece card card-back-alt">
    <h3>Professionally done for less than the rest</h3>
    <ul>
      <li>Commercial</li><li>Residential</li><li>Window washing</li><li>Green House</li>
      <li>Skylight</li><li>Gutter</li><li>Power washing</li><li>Fully insured</li>
    </ul>
  </section>
  <p class="label" style="left:19px;top:368px;width:173px">Back Card Option #2</p>

  <section class="piece letterhead lh-1">
    <svg class="band" style="top:0" width="272" height="80" viewBox="0 0 272 80" preserveAspectRatio="none">
      <defs><linearGradient id="hb1" x1="0" x2="1"><stop offset="0" stop-color="var(--blue-light)"/><stop offset="1" stop-color="var(--blue-deep)"/></linearGradient></defs>
      <path d="M0 0 H272 V62 Q150 38 0 56Z" fill="url(#hb1)"/>
      <path d="M0 56 Q150 38 272 62" stroke="var(--orange)" stroke-width="3" fill="none"/>
    </svg>
    <div class="lh-contact">2847 Tallow Bend Rd Norristown PA 19403<br>(610) 555-0147<br>wwwdw@brovalco-example.com<br>www.brovalco-example.com</div>
    <div class="brand"><span class="mark"></span>Brovalco Upkeep LLC</div>
    <svg class="band" style="bottom:0" width="272" height="6" viewBox="0 0 272 6" preserveAspectRatio="none"><rect width="272" height="6" fill="var(--blue)"/></svg>
    <p class="lh-footer">www.brovalco-example.com</p>
  </section>
  <p class="label" style="left:204px;top:410px;width:272px">Letterhead Option #1</p>

  <section class="piece letterhead lh-2">
    <svg class="band" style="top:0" width="272" height="80" viewBox="0 0 272 80" preserveAspectRatio="none">
      <defs><linearGradient id="hb2" x1="0" x2="1"><stop offset="0" stop-color="var(--blue-light)"/><stop offset="1" stop-color="var(--blue-deep)"/></linearGradient></defs>
      <path d="M0 0 H272 V62 Q150 38 0 56Z" fill="url(#hb2)"/>
      <path d="M0 56 Q150 38 272 62" stroke="var(--orange)" stroke-width="3" fill="none"/>
    </svg>
    <div class="brand"><span class="mark"></span>Brovalco Upkeep LLC</div>
    <svg class="band" style="bottom:0" width="272" height="6" viewBox="0 0 272 6" preserveAspectRatio="none"><rect width="272" height="6" fill="var(--blue)"/></svg>
    <p class="lh-footer">2847 Tallow Bend Rd Norristown PA 19403 · (610) 555-0147 · wwwdw@brovalco-example.com</p>
  </section>
  <p class="label" style="left:509px;top:410px;width:272px">Letterhead Option #2</p>

  <section class="piece envelope env-back">
    <svg class="band" style="top:0" width="293" height="92" viewBox="0 0 293 92" preserveAspectRatio="none">
      <rect width="293" height="92" fill="var(--paper-shade)"/>
      <path d="M0 0 H293 V20 L146 58 L0 20Z" fill="var(--orange)"/>
      <path d="M0 92 L120 45 M293 92 L173 45" stroke="#d6dbe2" stroke-width="1"/>
    </svg>
  </section>

  <section class="piece envelope env-plain-1">
    <svg class="band" style="top:0" width="293" height="92" viewBox="0 0 293 92" preserveAspectRatio="none">
      <rect width="293" height="92" fill="var(--paper)"/>
      <path d="M0 0 L146 52 L293 0" stroke="#cfd5dd" stroke-width="1" fill="none"/>
    </svg>
    <p class="env-url" style="top:56px">www.brovalco-example.com</p>
  </section>

  <section class="piece envelope env-plain-2">
    <svg class="band" style="top:0" width="293" height="92" viewBox="0 0 293 92" preserveAspectRatio="none">
      <rect width="293" height="92" fill="var(--paper)"/>
      <path d="M0 0 L146 48 L293 0" stroke="#cfd5dd" stroke-width="1" fill="none"/>
    </svg>
  </section>

  <section class="piece envelope env-front">
    <svg class="band" style="top:0" width="293" height="40" viewBox="0 0 293 40" preserveAspectRatio="none">
      <defs><linearGradient id="eb" x1="0" x2="1"><stop offset="0" stop-color="var(--blue-light)"/><stop offset="1" stop-color="var(--blue-deep)"/></linearGradient></defs>
      <path d="M0 0 H293 V30 Q160 14 0 28Z" fill="url(#eb)"/>
      <path d="M0 28 Q160 14 293 30" stroke="var(--orange)" stroke-width="2.5" fill="none"/>
    </svg>
    <div class="brand"><span class="mark"></span>Brovalco Upkeep LLC</div>
    <svg class="band" style="bottom:0" width="293" height="4" viewBox="0 0 293 4" preserveAspectRatio="none"><rect width="293" height="4" fill="var(--blue)"/></svg>
  </section>
  <p class="label" style="left:888px;top:421px;width:293px">Envelope Front &amp; Back</p>

</main>
</body>
</html>
```